Real Estate Brochure/ door flyer.

I am looking for a brochure that can be put in a plastic door hanger bag and distributed as I walk throughout neighborhoods. It should be mainly directed towards Sellers, but have a nod to Buyers as well since once sold, the person will need to buy.
I was planning on a tri fold brochure, but am open to other styles. I do have a bio, and am on the fence as to whether or not to include it.

Target Market(s)

Owners of residential homes and potential buyers of the same

Industry/Entity Type

Real Estate

Colors

Designer to choose colors to be used in the design.

Requirements
Must have
• The service promises I have made, our logo,
• My contact information, email and cell phone.
• I'm looking for something bright and clean looking.
• There is an equal housing opportunity symbol and Dwellmark symbol that is required by law, I am trying to find artwork for it. As well as "Not intended to solicit represented parties" has to be on the brochure somewhere.
Nice to have
• Photos of homeowner's in a nice home. I like mixed family relationships. Interracial, same sex couples and young couples just starting out.
Should not have
• Any form of deadline or timeline to respond.

```html
<!DOCTYPE html>
<html lang="en">
<head>
<meta charset="utf-8">
<title>Harborline Real Estate – Tri-fold Brochure</title>
<link href="https://fonts.googleapis.com/css2?family=Cinzel:wght@400;700&family=Lato:wght@400;700&display=swap" rel="stylesheet">
<style>
  :root{
    --crimson:#b51f2e;
    --crimson-deep:#8e1220;
    --wine:#6e1420;
    --ink:#1d1d1d;
    --charcoal:#2b2b2b;
    --paper:#ffffff;
    --mist:#ececec;
    --text:#2a2a2a;
    --stage:#ffffff;
  }
  *{box-sizing:border-box;margin:0;padding:0}
  html,body{width:1200px;height:900px;overflow:hidden;background:var(--stage)}
  body{position:relative;font-family:"Lato",Arial,sans-serif;color:var(--text)}
  .brochure{position:absolute;left:112px;top:57px;width:985px;height:766px;display:flex;box-shadow:0 4px 14px rgba(0,0,0,.28)}
  .panel{position:relative;height:100%;overflow:hidden}
  .panel svg.bg{position:absolute;left:0;top:0}

  /* left panel */
  .panel--agent{width:337px;background:linear-gradient(#fafafa 40%,#e4e4e4)}
  .agent-name{position:absolute;left:86px;top:380px;width:169px;height:24px;border-radius:12px;background:var(--wine);
    color:#fff;font-family:"Cinzel",Georgia,serif;font-weight:700;font-size:13px;letter-spacing:.5px;text-align:center;line-height:24px}
  .agent-bio{position:absolute;left:24px;top:430px;width:296px;font-size:10.6px;line-height:13.6px;text-align:justify;color:var(--text)}
  .agent-bio h3{margin-top:8px;color:var(--crimson);font-size:11.4px;font-weight:700;line-height:13px;text-align:left}
  .agent-bio p+p{margin-top:2px}
  .call-pill{position:absolute;left:39px;top:697px;width:252px;height:29px;border-radius:15px;background:var(--charcoal);
    color:#fff;font-family:"Cinzel",Georgia,serif;font-size:19px;text-align:center;line-height:29px;letter-spacing:.5px}

  /* middle panel */
  .panel--since{width:323px;background:linear-gradient(#c2303d 0%,#b8202e 45%,#a3101f 100%);color:#fff;text-align:center}
  .since-title{position:absolute;top:78px;width:100%;font-family:"Cinzel",Georgia,serif;font-size:38px;letter-spacing:1px;line-height:40px}
  .since-sub{position:absolute;top:118px;width:100%;font-family:"Cinzel",Georgia,serif;font-size:12.5px;letter-spacing:.4px}
  .office{position:absolute;top:630px;width:100%;font-size:12px;line-height:17.5px}
  .office .office-name{font-family:"Cinzel",Georgia,serif;font-weight:700;font-size:15px;letter-spacing:.4px;margin-bottom:2px}
  .office .office-web{font-family:"Cinzel",Georgia,serif;font-weight:700;font-size:11.5px;margin-top:4px;letter-spacing:.3px}

  /* right panel */
  .panel--cover{width:325px;background:linear-gradient(#fff 60%,#ececec)}
  .brand-name{position:absolute;top:68px;width:100%;text-align:center;font-family:"Cinzel",Georgia,serif;font-weight:700;
    color:var(--wine);font-size:26px;line-height:27px;letter-spacing:1px}
  .brand-name small{display:block;font-size:17px;letter-spacing:3px}
  .cover-line{position:absolute;top:626px;width:100%;text-align:center;font-family:"Cinzel",Georgia,serif;color:var(--ink);font-size:20.5px;letter-spacing:.5px}
  .cover-line strong{display:block;color:var(--crimson);font-weight:700;font-size:26px;line-height:32px}
  .web-pill{position:absolute;left:56px;top:700px;width:225px;height:23px;border-radius:12px;background:var(--wine);color:#fff;
    font-family:"Cinzel",Georgia,serif;font-weight:700;font-size:11px;text-align:center;line-height:23px;letter-spacing:.3px}
</style>
</head>
<body>
<main class="brochure">

  <section class="panel panel--agent">
    <svg class="bg" width="337" height="766" viewBox="0 0 337 766">
      <defs>
        <linearGradient id="houseTone" x1="0" y1="0" x2="0" y2="1">
          <stop offset="0" stop-color="#dfe3e6"/><stop offset=".55" stop-color="#9aa3a3"/><stop offset="1" stop-color="#5d7a3c"/>
        </linearGradient>
        <radialGradient id="portraitTone"><stop offset="0" stop-color="#d7a78d"/><stop offset="1" stop-color="#8a6a55"/></radialGradient>
      </defs>
      <path role="img" aria-label="Photo of a large two-storey house with a wraparound porch on a green lawn" d="M0 18 H337 V215 C250 225 150 262 0 300 Z" fill="url(#houseTone)"/>
      <path d="M0 300 C150 262 250 225 337 215 V236 C250 244 150 282 0 320 Z" fill="var(--charcoal)"/>
      <path d="M0 320 C150 282 250 244 337 236 V241 C250 250 150 288 0 326 Z" fill="var(--crimson)"/>
      <circle cx="166" cy="273" r="88" fill="#fff"/>
      <circle cx="166" cy="273" r="84" fill="none" stroke="var(--crimson-deep)" stroke-width="4"/>
      <circle role="img" aria-label="Portrait photo of the agent" cx="166" cy="273" r="78" fill="url(#portraitTone)"/>
    </svg>
    <div class="agent-name">DANIEL HARTWELL</div>
    <div class="agent-bio">
      <p>Since 1983, I have been buying and selling real estate, specializing in income producing multi-family properties as well as single family rehab/flip type properties. I became a Dwellmark in 2007, where I have been able to use my experiences in real estate investing to help contractors as well as first time home buyers to realize their home ownership and investment goals. Keeping in line with “helping others”, I feel it a moral obligation to help those less fortunate among us; to “give back” as the saying goes. I work with and support the following organizations:</p>
      <h3>VALLEY ALLIANCE OF RESIDENTIAL CARE HOMES (VARCH)</h3>
      <p>I am the Treasurer of this organization which provides 1,600 beds, in one hundred homes across the State of Connecticut providing housing to mentally and physically disabled people of our communities</p>
    </div>
    <div class="call-pill">CALL-860-555-0148</div>
  </section>

  <section class="panel panel--since">
    <svg class="bg" width="323" height="766" viewBox="0 0 323 766">
      <defs>
        <linearGradient id="homeTint" x1="0" y1="0" x2="0" y2="1">
          <stop offset="0" stop-color="#fff" stop-opacity="0"/><stop offset=".5" stop-color="#fff" stop-opacity=".14"/><stop offset="1" stop-color="#fff" stop-opacity="0"/>
        </linearGradient>
      </defs>
      <rect role="img" aria-label="Faded red-toned photo of a gabled family house with trees and garden" x="0" y="150" width="323" height="440" fill="url(#homeTint)"/>
    </svg>
    <h1 class="since-title">SINCE 1983</h1>
    <p class="since-sub">BUYING AND SELLING REAL ESTATE</p>
    <div class="office">
      <div class="office-name">Harborline Real Estate LLC</div>
      <div>118 Maple Row</div>
      <div>Millbrook, CT 06100</div>
      <div>call-860-555-0148</div>
      <div class="office-web">WWW.HARBORLINEREALESTATE.COM</div>
    </div>
  </section>

  <section class="panel panel--cover">
    <svg class="bg" width="325" height="766" viewBox="0 0 325 766">
      <defs>
        <linearGradient id="familyTone" x1="0" y1="0" x2="1" y2="1">
          <stop offset="0" stop-color="#cfd9e0"/><stop offset=".6" stop-color="#b9b3ad"/><stop offset="1" stop-color="#8c8a88"/>
        </linearGradient>
        <radialGradient id="handTone"><stop offset="0" stop-color="#b5754c"/><stop offset="1" stop-color="#e9c9b0"/></radialGradient>
      </defs>
      <path d="M0 205 C120 203 255 170 325 88 V118 C265 190 135 213 0 215 Z" fill="var(--crimson)"/>
      <path role="img" aria-label="Photo of a smiling family of four standing in front of their modern home" d="M0 212 C135 210 265 188 325 120 V545 C250 520 120 470 0 430 Z" fill="url(#familyTone)"/>
      <path d="M0 430 C120 470 250 520 325 545 V560 C250 540 120 490 0 448 Z" fill="var(--ink)"/>
      <circle cx="101" cy="500" r="82" fill="#fff"/>
      <circle cx="101" cy="500" r="78" fill="none" stroke="var(--crimson-deep)" stroke-width="4"/>
      <circle role="img" aria-label="Photo of an open hand holding a small model house" cx="101" cy="500" r="72" fill="url(#handTone)"/>
    </svg>
    <div class="brand-name">HARBORLINE<small>REAL ESTATE</small></div>
    <h2 class="cover-line">FIND THE PERFECT HOME<strong>FOR YOUR FAMILY</strong></h2>
    <div class="web-pill">WWW.HARBORLINEREALESTATE.COM</div>
  </section>

</main>
</body>
</html>
```